Modern, Bright Bubble Bath Label

We need a label design for a private label bubble bath we will begin selling.

We will have 8 different scents of bubble bath. Each has a color associated with it as follows: Napa Valley Grape (Purple), Mixed Berry (Blue), Bartlett Pear (Green), Sweet Pineapple (Yellow), Juicy Peach (Orange), Red Raspberry (Red), Creamy Coconut (Brown or White), Kiwi Watermelon (Pink). So what we want is 8 different bottle labels. The labels CAN be different, but they will likely be the same label, just with a different color and different text (scent name).

Labels should be bright, fun, modern, and clean. The main color should be what is listed above, but other colors can be incorporated, as can be seen in the attachments.

Label should be between 2.5" and 3.5" tall, and 7.25" wide. This will be applied to an 8oz boston round, plastic, transparent bottle with a black cap.

For reference, I love The Lotus Loft packaging designs.

Women

Hair And Beauty

Copper Fern

Serif
Sans Serif

• -Company Logo: 'Copper Fern', which will need to be designed by the winning designer. You can simply put 'Copper Fern' in the label for now as a place holder.
• -Text 'Sparkling Bubble Bath'
• -Name of Scent
• -Packaging that is brightly colored and associated with the scent as mentioned in the product description.
• Should be in format that can be edited in Adobe Photoshop. We will add additional text and details (ingredients, description, etc.) in Photoshop once we choose the winning design
• Picture or graphic of associated fruit

```html
<!DOCTYPE html>
<html lang="en">
<head>
<meta charset="UTF-8">
<title>Copper Fern Sparkling Bubble Bath – Napa Valley Grape</title>
<link rel="stylesheet" href="https://fonts.googleapis.com/css2?family=Cabin:wght@400;500&family=Open+Sans:wght@400&family=Yellowtail&display=swap">
<style>
  :root {
    --page: #ffffff;
    --grape: #840a8a;
    --ink-light: #ffffff;
    --scent-bar: #dcdcdc;
    --scent-ink: #6a1270;
    --fruit-light: #f6eef7;
    --fruit-mid: #c79bcc;
  }
  * { margin: 0; padding: 0; box-sizing: border-box; }
  html, body {
    width: 1101px;
    height: 1200px;
    overflow: hidden;
    background: var(--page);
  }
  .canvas {
    position: relative;
    width: 1101px;
    height: 1200px;
  }
  .label {
    position: absolute;
    left: 121px;
    top: 193px;
    width: 858px;
    height: 855px;
    background: var(--grape);
    overflow: hidden;
  }
  .brand {
    position: absolute;
    left: 285px;
    top: 41px;
    width: 295px;
    height: 103px;
    border: 3px solid var(--ink-light);
    border-radius: 52px;
    display: flex;
    align-items: center;
    justify-content: center;
    gap: 12px;
  }
  .brand-name {
    font-family: "Cabin", sans-serif;
    font-weight: 400;
    font-size: 40px;
    color: var(--ink-light);
    letter-spacing: 0.5px;
  }
  .brand-dot {
    width: 22px;
    height: 22px;
    border-radius: 50%;
    background: var(--ink-light);
  }
  .product-title {
    position: absolute;
    left: 0;
    top: 195px;
    width: 100%;
    text-align: center;
    color: var(--ink-light);
  }
  .product-title .headline {
    display: block;
    font-family: "Yellowtail", cursive;
    font-size: 128px;
    line-height: 1;
    margin-left: -20px;
  }
  .product-title .subline {
    display: block;
    font-family: "Open Sans", sans-serif;
    font-size: 38px;
    line-height: 1;
    margin-top: -18px;
    letter-spacing: 1px;
  }
  .scent-name {
    position: absolute;
    left: 154px;
    top: 419px;
    width: 558px;
    height: 89px;
    background: var(--scent-bar);
    display: flex;
    align-items: center;
    justify-content: center;
    font-family: "Cabin", sans-serif;
    font-weight: 400;
    font-size: 41px;
    color: var(--scent-ink);
  }
  .fruit-art {
    position: absolute;
    left: 290px;
    top: 535px;
    width: 286px;
    height: 286px;
    border-radius: 50%;
    background: radial-gradient(circle at 50% 55%, var(--fruit-mid) 0%, var(--fruit-light) 62%, var(--ink-light) 80%);
  }
</style>
</head>
<body>
  <main class="canvas">
    <section class="label">
      <div class="brand">
        <span class="brand-name">Copper Fern</span>
        <span class="brand-dot"></span>
      </div>
      <h1 class="product-title">
        <span class="headline">Sparkling</span>
        <span class="subline">Bubble Bath</span>
      </h1>
      <p class="scent-name">Napa Valley Grape</p>
      <div class="fruit-art" role="img" aria-label="Illustration of a bunch of purple grapes with a green leaf and brown stem on a white circle"></div>
    </section>
  </main>
</body>
</html>
```